Established food business needs a new name card design

Refer to attached current name card. Would like a new professional look design with only the company name and logo without any pictures. Would like green and yellow to be included.
To include:
My name "IBRAHIM SUKRI" and hand phone number "87260413".
To delete "
"Along Brackendale Ave 8" and
"www.nur-tiwas.com.sg"
To change email to:
"tkr27@velmorix.com.sg"

```html
<!DOCTYPE html>
<html lang="en">
<head>
<meta charset="utf-8">
<title>NUR-TIWAS name card</title>
<link href="https://fonts.googleapis.com/css2?family=Montserrat:wght@600&family=Questrial&display=swap" rel="stylesheet">
<style>
  :root {
    --backdrop: #262626;
    --card-white: #ffffff;
    --card-green: #294735;
    --brand-yellow: #e8c638;
    --text-grey: #5a5a5a;
    --on-green: #ffffff;
  }
  * { margin: 0; padding: 0; box-sizing: border-box; }
  html, body {
    width: 1200px;
    height: 800px;
    overflow: hidden;
    background: var(--backdrop);
  }
  .canvas {
    position: relative;
    width: 1200px;
    height: 800px;
  }
  .card {
    position: absolute;
    left: 316px;
    width: 570px;
    height: 330px;
    box-shadow: 0 6px 18px rgba(0, 0, 0, 0.45);
  }
  .card-front {
    top: 50px;
    background: var(--card-white);
  }
  .card-back {
    top: 418px;
    background: var(--card-green);
    display: flex;
    align-items: center;
    justify-content: center;
  }
  .brand {
    display: flex;
    align-items: center;
    gap: 10px;
    font-family: "Montserrat", sans-serif;
    font-weight: 600;
    letter-spacing: 0.02em;
  }
  .brand-dot {
    border-radius: 50%;
    background: var(--brand-yellow);
  }
  .brand-front {
    position: absolute;
    left: 34px;
    top: 68px;
    color: var(--brand-yellow);
    font-size: 20px;
  }
  .brand-front .brand-dot { width: 34px; height: 34px; }
  .brand-back {
    color: var(--on-green);
    font-size: 38px;
    gap: 18px;
  }
  .brand-back .brand-dot { width: 70px; height: 70px; }
  .contact {
    position: absolute;
    left: 34px;
    top: 194px;
    font-family: "Questrial", sans-serif;
    color: var(--text-grey);
  }
  .contact-name {
    font-family: "Montserrat", sans-serif;
    font-weight: 600;
    font-size: 15.5px;
    color: var(--brand-yellow);
    letter-spacing: 0.03em;
  }
  .contact-role {
    margin-top: 6px;
    font-size: 14px;
    font-style: italic;
  }
  .contact-line {
    font-size: 13.5px;
    line-height: 22px;
  }
  .contact-phone { margin-top: 12px; }
</style>
</head>
<body>
  <main class="canvas">
    <section class="card card-front" aria-label="Name card front">
      <div class="brand brand-front">
        <span class="brand-dot"></span>
        <span class="brand-name">NUR-TIWAS</span>
      </div>
      <div class="contact">
        <p class="contact-name">IBRAHIM SUKRI</p>
        <p class="contact-role">Manager</p>
        <p class="contact-line contact-phone">87260413</p>
        <p class="contact-line contact-email">tkr27@velmorix.com.sg</p>
      </div>
    </section>
    <section class="card card-back" aria-label="Name card back">
      <div class="brand brand-back">
        <span class="brand-dot"></span>
        <span class="brand-name">NUR-TIWAS</span>
      </div>
    </section>
  </main>
</body>
</html>
```